8'x8' Exhibit Backdrop for Healthcare Events focused on the 55 and older crowds

8X8 Backdrop for Exhibiting.

I also want a design for a 6' table skirt to include our logo on two sides and the logo with Hereditary Cancer Screening underneath on the front. I want the main message of Will You Give your Loved Ones The Information To Beat Cancer in Their Lives to be completely centered on the 8X8 backdrop. Hereditary Cancer Screening The Test You Take For Them in the top left corner and the purple box on the right hand side - just like the photo that has been uploaded below. I need High resolution photos around the backdrop but not so large that they overtake the main message.

Target Market(s)

55+ crowd living in Adult only communities. They have an active lifestyle

Industry/Entity Type

Healthcare

Other font styles liked:
• "The Test You Take For Them" is Comic Sans

Colors
0255a3
fbed22
ffffff

Requirements
Must have
• I am posting a photo of the exact backdrop I would like to see. There are red arrows showing where to move certain items. There is a space underneath the slogan WILL YOU GIVE YOUR LOVED ONES... where another photo will go. Add another photo underneath the slogan that you are moving up - GIVE THEM THE GIFT OF KNOWLEDGE
• See the upload section for the new photo
• Do this one exactly like I am asking for and then you can show me some of your ideas. Thanks
• THE PHOTOS UPLOADED ARE EXAMPLES. FEEL FREE TO SEARCH OUT YOUR OWN HIGH RESOLUTION PHOTOS. THANKS

```html
<!DOCTYPE html>
<html lang="en">
<head>
<meta charset="utf-8">
<title>Hereditary Cancer Screening – Exhibit Backdrop</title>
<link rel="stylesheet" href="https://fonts.googleapis.com/css2?family=Arimo:wght@400;700&family=Comic+Neue:wght@400&family=Lato:wght@400;700&family=Roboto+Condensed:wght@400;700&display=swap">
<style>
  :root {
    --navy: #1c2576;
    --green: #66ee2c;
    --ink: #111111;
    --white: #ffffff;
    --band: #0c0c0c;
  }
  html, body {
    margin: 0;
    padding: 0;
    width: 1200px;
    height: 1200px;
    overflow: hidden;
    background: var(--white);
  }
  .backdrop {
    position: relative;
    width: 1200px;
    height: 1200px;
    background: var(--white);
    font-family: "Roboto Condensed", "Arial Narrow", sans-serif;
    color: var(--ink);
  }
  .title {
    position: absolute;
    left: 28px;
    top: 30px;
    margin: 0;
    font-family: "Arimo", Arial, sans-serif;
    color: var(--navy);
    line-height: 0.98;
    font-weight: 400;
  }
  .title__strong { display: block; font-weight: 700; font-size: 66px; letter-spacing: -0.5px; }
  .title__line { display: block; font-size: 70px; letter-spacing: -0.5px; }
  .tagline {
    position: absolute;
    left: 6px;
    top: 288px;
    width: 378px;
    height: 32px;
    background: var(--green);
    color: var(--white);
    font-family: "Comic Neue", "Comic Sans MS", cursive;
    font-size: 23px;
    line-height: 32px;
    text-align: center;
  }
  .photo { position: absolute; margin: 0; }
  .photo--family   { left: 412px; top: 22px;  width: 318px; height: 322px; background: linear-gradient(160deg, #8fae6a 0%, #e9d7c4 45%, #c9a88c 100%); }
  .photo--pair-a   { left: 738px; top: 18px;  width: 208px; height: 158px; background: linear-gradient(135deg, #6b4a3a 0%, #c7977b 55%, #efe4da 100%); }
  .photo--pair-b   { left: 954px; top: 12px;  width: 226px; height: 164px; background: linear-gradient(135deg, #5a5a5a 0%, #b7b7b7 55%, #f0f0f0 100%); }
  .photo--trio     { left: 738px; top: 184px; width: 208px; height: 160px; background: linear-gradient(135deg, #3e3e3e 0%, #a9a9a9 55%, #e6e6e6 100%); }
  .photo--grand    { left: 954px; top: 184px; width: 226px; height: 162px; background: linear-gradient(135deg, #e8dccf 0%, #d2a58a 50%, #5b78b8 100%); }
  .photo--mother   { left: 646px; top: 356px; width: 534px; height: 360px; background: linear-gradient(150deg, #d8c6ae 0%, #b8643b 40%, #eadbd0 75%, #c49a82 100%); }
  .photo--reading  { left: 646px; top: 728px; width: 534px; height: 400px; background: linear-gradient(150deg, #c7a289 0%, #e6b48f 35%, #2a3656 70%, #8a7a6e 100%); }

  .headline {
    position: absolute;
    inset: 0;
    margin: 0;
    font-weight: 400;
    text-transform: uppercase;
    pointer-events: none;
  }
  .headline span { position: absolute; white-space: nowrap; }
  .headline__row {
    left: 28px;
    font-size: 80px;
    line-height: 1;
    letter-spacing: -2px;
  }
  .headline__row--give  { top: 362px; }
  .headline__row--loved { top: 448px; }
  .headline__row strong { font-weight: 700; }
  .headline__band {
    left: 6px;
    top: 534px;
    width: 598px;
    box-sizing: border-box;
    padding-left: 22px;
    background: var(--band);
    color: var(--white);
    font-size: 48px;
    line-height: 56px;
  }
  .headline__cancer {
    left: 22px;
    top: 600px;
    color: var(--green);
    font-size: 172px;
    line-height: 0.86;
    letter-spacing: -4px;
  }
  .headline__lives {
    left: 28px;
    top: 758px;
    font-size: 84px;
    line-height: 1;
    letter-spacing: -2px;
  }
  .message {
    position: absolute;
    left: 6px;
    top: 862px;
    width: 598px;
    height: 118px;
    padding: 14px 0 0 22px;
    background: var(--band);
    color: var(--white);
    font-family: "Lato", Arial, sans-serif;
    text-transform: uppercase;
    box-sizing: border-box;
  }
  .message__lead { margin: 0; font-size: 27px; line-height: 32px; letter-spacing: -0.3px; }
  .message__line { margin: 0; font-size: 21px; line-height: 25px; letter-spacing: -0.3px; }

  .brand {
    position: absolute;
    left: 34px;
    top: 1008px;
    display: flex;
    align-items: center;
    gap: 14px;
  }
  .brand__mark { width: 62px; height: 62px; }
  .brand__name {
    font-family: "Lato", Arial, sans-serif;
    font-weight: 700;
    font-size: 26px;
    line-height: 26px;
    color: var(--navy);
    text-transform: uppercase;
    letter-spacing: 1px;
  }
  .site {
    position: absolute;
    right: 22px;
    top: 1150px;
    font-family: "Lato", Arial, sans-serif;
    font-weight: 700;
    font-size: 26px;
    color: var(--ink);
  }
</style>
</head>
<body>
<main class="backdrop">
  <h1 class="title">
    <span class="title__strong">Hereditary</span>
    <span class="title__line">Cancer</span>
    <span class="title__line">Screening</span>
  </h1>
  <div class="tagline">"The Test You Take For Them"</div>

  <figure class="photo photo--family" role="img" aria-label="Photo of a multi-generation family smiling together outdoors"></figure>
  <figure class="photo photo--pair-a" role="img" aria-label="Photo of a grandfather hugging his granddaughter"></figure>
  <figure class="photo photo--pair-b" role="img" aria-label="Black and white photo of a grandmother embraced by a young girl"></figure>
  <figure class="photo photo--trio" role="img" aria-label="Black and white photo of grandparents with a smiling girl"></figure>
  <figure class="photo photo--grand" role="img" aria-label="Photo of grandparents laughing with their grandchildren"></figure>
  <figure class="photo photo--mother" role="img" aria-label="Photo of a smiling red-haired woman looking down"></figure>
  <figure class="photo photo--reading" role="img" aria-label="Photo of a grandfather reading a book with a young child and a baby"></figure>

  <h2 class="headline">
    <span class="headline__row headline__row--give">Will you <strong>give</strong></span>
    <span class="headline__row headline__row--loved">your loved ones</span>
    <span class="headline__band">The information to beat</span>
    <span class="headline__cancer">Cancer</span>
    <span class="headline__lives">In their lives ?</span>
  </h2>

  <div class="message">
    <p class="message__lead">Give them the gift of knowledge</p>
    <p class="message__line">Knowing is better than not knowing.</p>
    <p class="message__line">Knowledge is power</p>
  </div>

  <div class="brand">
    <svg class="brand__mark" viewBox="0 0 62 62" aria-hidden="true">
      <circle cx="31" cy="31" r="28" fill="none" stroke="var(--navy)" stroke-width="4"/>
    </svg>
    <div class="brand__name">Kinward<br>Health<br>Group</div>
  </div>

  <div class="site">www.kinshipscreening.com</div>
</main>
</body>
</html>
```